Briefpapier für IT-Dienstleister
Zielgruppe
Hallo wir sind IT Dienstleister und Verkaufen viel Hard- und Software, jedoch liegt der Fokus auf IT-Security und Netzwerkaustattung.
Die Zielgruppe sind ausschliesslich Geschäftskunden aus Klein und Großunternehmen.
New Homepage(name): https://velor-netz.de
Old homepage(name): https://kornwerk.de
Aufgabenstellung
Das Briefpapier soll den Namen und unser Logo 'velor IT netz' behinhalten.
Homepage: https://www.velor-netz.de
main name = velor IT netz
Die Firmenadresse(Footer) bleibt jedoch gleich: Kornwerk Elektrotechnik GmbH & Co. Vertriebs KG

```html
<!DOCTYPE html>
<html lang="de">
<head>
<meta charset="utf-8">
<title>Briefpapier – velor IT netz</title>
<link rel="stylesheet" href="https://fonts.googleapis.com/css2?family=Oswald:wght@300;600&display=swap">
<style>
  :root {
    --paper: #ffffff;
    --ink: #2b2b2b;
    --logo-ink: #111111;
    --mark: #9a9a9a;
  }
  html, body {
    margin: 0;
    padding: 0;
    overflow: hidden;
    background: var(--paper);
  }
  .letterhead {
    position: relative;
    width: 848px;
    height: 1200px;
    background: var(--paper);
    overflow: hidden;
    font-family: "Oswald", "Arial Narrow", sans-serif;
    font-weight: 300;
    color: var(--ink);
  }
  .info-block {
    position: absolute;
    left: 634px;
    margin: 0;
    font-size: 12.5px;
    line-height: 16px;
    letter-spacing: -0.1px;
    font-style: normal;
    white-space: nowrap;
  }
  .company-line { top: 31px; }
  .contact { top: 139px; }
  .legal { top: 1025px; }
  .bank { top: 1136px; }
  .brand {
    position: absolute;
    right: 20px;
    top: 58px;
    display: flex;
    align-items: center;
    gap: 12px;
    font-family: "Oswald", "Arial Narrow", sans-serif;
    font-weight: 600;
    font-size: 50px;
    line-height: 1;
    letter-spacing: -0.5px;
    color: var(--logo-ink);
  }
  .brand-square {
    width: 14px;
    height: 14px;
    background: var(--logo-ink);
  }
  .fold-mark {
    position: absolute;
    left: 0;
    height: 1px;
    background: var(--mark);
  }
  .fold-top { top: 429px; width: 12px; }
  .punch-mark { top: 607px; width: 25px; }
  .fold-bottom { top: 858px; width: 12px; }
</style>
</head>
<body>
  <main class="letterhead">
    <p class="info-block company-line">
      Kornwerk Elektrotechnik GmbH &amp; Co. Vertriebs KG<br>
      Vertrieb von Elektrionik &amp; Lichttechnik
    </p>

    <div class="brand" aria-label="velor IT netz">
      <span class="brand-square"></span>
      <span class="brand-name">velor IT netz</span>
    </div>

    <address class="info-block contact">
      Lindenweg 12, D-63199 Talbach<br>
      Postfach 2740, D-63191 Talbach<br>
      Telefon +49 6190 555210<br>
      Telefax +49 6190 555219<br>
      info@kornwerk.de<br>
      www.velor-netz.de
    </address>

    <span class="fold-mark fold-top"></span>
    <span class="fold-mark punch-mark"></span>
    <span class="fold-mark fold-bottom"></span>

    <p class="info-block legal">
      Handelsregister Talbach 5 HRA 4471<br>
      Persöhnlich haftende Gesellschaft:<br>
      Kornwerk Elektrotechnik Beteiligungs GmbH<br>
      Geschäftsführer: Dipl. Ing. Jonas Kastel<br>
      Handelsregister Talbach 5 HRB 5829<br>
      SteuerNr. 31/582/40917
    </p>

    <p class="info-block bank">
      Bankverbindung: Talbacher Volksbank<br>
      IBAN DE00 0000 0000 xxxx x xxxx<br>
      SWIFT / BIC: TALBDEXX<br>
      Umsatzsteuer-ID: DE000000000
    </p>
  </main>
</body>
</html>
```